THORNWICK COVE RUM - Premium Gold Rum Needs New Label

We would like a better label that we currently have for our Gold Rum that won the bronze medal in the 2003 Velmora Spirits Gala. We have called it "Thornwick Cove Rum" as our distillery is based here in Golden bay, New Zealand. The first recorded siting of New Zealand was made by Corin Velde and while anchored in the bay erupted in a terrible bloodshed with the natives. Corin Velde and his crew fled without setting foot on land. See attached back label for more on this story or google it! We have only a few thousand litres of the award winning rum and once sold out intend to import rum from Barbados and continue to sell it as "Thornwick Cove Rum" so the award winning aspect will be lost. We do not wish to change the label at that time but instead simply use stickers on the bottles containing the award winning rum and once sold out of the award running rum continue without the stickers. I think that there is a lot of imagery to draw and that the name is great! We want to see it in all the cool bars and bottle stores in New Zealand and Australia. It will be a premium product but we do not want to use a bespoke bottle. I attach pictures of our existing bottle and label and also dimensions and specs of the bottle that we will be using going forward. The bottle is the "quill" bottle - see numbers 3 and 4 on the attached spec sheet. We will most likely use with a cork ie bottle 4.
Target Market(s)
Up and coming professional males, 25-35, the cool cats who drink at the cool bars.
Requirements
Must have
- Must state: 40% ALC/VOL, Bottled by: Pellow Finch Distillery, 17b Harrowgate Lane, Takaka, Golden Bay, New Zealand, bar code Must also have some embossing/texture on the label
Should not have
- See "Grimwald Rum" - recently released - let's not look like them please.

```html
<!DOCTYPE html>
<html lang="en">
<head>
<meta charset="utf-8">
<title>Thornwick Cove Gold Rum – Label</title>
<link rel="stylesheet" href="https://fonts.googleapis.com/css2?family=Cinzel:wght@400;500&family=Federo&display=swap">
<style>
  :root {
    --page-bg: #f3f3f3;
    --label-bg: #e2e2e2;
    --label-bg-light: #ececec;
    --etching-dark: #a9a9a9;
    --etching-light: #d4d4d4;
    --seal-black: #141414;
    --seal-grey: #2a2a2a;
    --ink-white: #f4f4f4;
    --rule-grey: #9a9a9a;
  }
  * { box-sizing: border-box; margin: 0; padding: 0; }
  html, body {
    width: 1200px;
    height: 1000px;
    overflow: hidden;
    background: var(--page-bg);
  }
  .canvas {
    position: relative;
    width: 1200px;
    height: 1000px;
  }
  .label {
    position: absolute;
    left: 175px;
    top: 130px;
    width: 850px;
    height: 740px;
    background: linear-gradient(180deg, var(--label-bg-light), var(--label-bg));
    box-shadow: 0 4px 14px rgba(0,0,0,0.25);
    overflow: hidden;
  }
  .ship-etching {
    position: absolute;
    top: 0;
    width: 300px;
    height: 100%;
  }
  .ship-etching--left {
    left: 0;
    background: linear-gradient(100deg, var(--etching-dark) 0%, var(--etching-light) 55%, var(--label-bg-light) 100%);
  }
  .ship-etching--right {
    right: 0;
    background: linear-gradient(260deg, var(--etching-dark) 0%, var(--etching-light) 55%, var(--label-bg-light) 100%);
  }
  .seal {
    position: absolute;
    left: 140px;
    top: 85px;
    width: 570px;
    height: 570px;
    border-radius: 50%;
    background: radial-gradient(circle at 50% 45%, var(--seal-grey), var(--seal-black) 70%);
    box-shadow: 0 0 0 3px var(--seal-black);
  }
  .seal__ring {
    position: absolute;
    inset: 10px;
    border-radius: 50%;
    border: 3px solid var(--ink-white);
  }
  .seal__abv {
    position: absolute;
    top: 48px;
    width: 100%;
    text-align: center;
    font-family: "Cinzel", serif;
    font-size: 15px;
    letter-spacing: 3px;
    color: #bdbdbd;
  }
  .seal__swords {
    position: absolute;
    left: 225px;
    top: 85px;
    width: 120px;
    height: 70px;
    background: linear-gradient(180deg, #e8e8e8, #bcbcbc);
    border-radius: 6px;
  }
  .seal__name {
    position: absolute;
    top: 212px;
    width: 100%;
    text-align: center;
    font-family: "Federo", sans-serif;
    font-size: 66px;
    letter-spacing: 2px;
    color: var(--ink-white);
  }
  .seal__rule {
    position: absolute;
    left: 40px;
    width: 490px;
    height: 2px;
    background: var(--rule-grey);
  }
  .seal__rule--top { top: 200px; }
  .seal__rule--bottom { top: 306px; }
  .seal__flourish {
    position: absolute;
    left: 205px;
    top: 345px;
    width: 160px;
    height: 44px;
    background: linear-gradient(90deg, #cfcfcf, #f2f2f2, #cfcfcf);
    border-radius: 22px;
  }
  .seal__product {
    position: absolute;
    top: 420px;
    width: 100%;
    text-align: center;
    font-family: "Cinzel", serif;
    font-weight: 400;
    font-size: 36px;
    letter-spacing: 5px;
    color: var(--ink-white);
  }
</style>
</head>
<body>
  <main class="canvas">
    <section class="label">
      <div class="ship-etching ship-etching--left" role="img" aria-label="Engraved sketch of a tall sailing ship's hull and rigging, grey line work"></div>
      <div class="ship-etching ship-etching--right" role="img" aria-label="Engraved sketch of a second sailing ship with masts and rigging, grey line work"></div>

      <div class="seal">
        <div class="seal__ring"></div>
        <p class="seal__abv">40% ALC/VOL</p>
        <div class="seal__swords" role="img" aria-label="Two crossed cutlasses emblem in white"></div>
        <div class="seal__rule seal__rule--top"></div>
        <h1 class="seal__name">Thornwick Cove</h1>
        <div class="seal__rule seal__rule--bottom"></div>
        <div class="seal__flourish" role="img" aria-label="White scroll flourish ornament"></div>
        <p class="seal__product">GOLD RUM</p>
      </div>
    </section>
  </main>
</body>
</html>
```